Business Card Design Project

Create an impressive business care to use
Updates

My logo is available at http://kestravolt.com, or

Industry/Entity Type

Business

Requirements
Must have
• company logo

```html
<!DOCTYPE html>
<html lang="en">
<head>
<meta charset="utf-8">
<title>Kestravolt Research Corporation – Business Card</title>
<link href="https://fonts.googleapis.com/css2?family=Source+Sans+3:wght@400;600;700&family=Noto+Sans+SC:wght@400&display=swap" rel="stylesheet">
<style>
  :root {
    --backdrop: #7a3212;
    --card: #ffffff;
    --ink-dark: #1c1c1c;
    --ink-grey: #8a8a8a;
    --ink-label: #6f6f6f;
    --rule: #d6d6d6;
    --brand-green: #2fa36b;
  }
  * { box-sizing: border-box; margin: 0; padding: 0; }
  html, body {
    width: 1200px; height: 789px; overflow: hidden;
    background: var(--backdrop);
    font-family: "Source Sans 3", "Noto Sans SC", sans-serif;
  }
  .canvas { position: relative; width: 1200px; height: 789px; }
  .card {
    position: absolute; top: 235px;
    width: 540px; height: 320px;
    background: var(--card);
    box-shadow: 0 6px 18px rgba(0,0,0,.35);
  }
  .card--front { left: 40px; }
  .card--back { left: 620px; }

  .brand { display: flex; align-items: center; justify-content: center; gap: 10px; }
  .brand-dot { width: 18px; height: 18px; border-radius: 50%; background: var(--brand-green); }
  .brand-name { font-weight: 600; color: var(--ink-dark); letter-spacing: 3px; line-height: 1; }

  .card--front .brand { position: absolute; top: 38px; left: 0; right: 0; }
  .card--front .brand-name { font-size: 30px; }

  .holder {
    position: absolute; top: 100px; left: 0; right: 0;
    text-align: center; color: var(--ink-grey); line-height: 1.25;
  }
  .holder-name { font-weight: 700; font-size: 15px; }
  .holder-cn, .holder-role { font-size: 14px; }

  .rule { position: absolute; height: 1px; background: var(--rule); }
  .rule--upper { top: 94px; left: 290px; right: 24px; }
  .rule--lower { top: 196px; left: 24px; right: 290px; }

  .office {
    position: absolute; font-size: 12.5px; color: var(--ink-grey); line-height: 17px;
  }
  .office--us { top: 204px; left: 24px; }
  .office--cn { top: 160px; left: 290px; }
  .office-label { font-weight: 700; color: var(--ink-label); font-size: 13px; }

  .card--back .brand { position: absolute; top: 130px; left: 0; right: 0; }
  .card--back .brand-name { font-size: 40px; }
  .back-url {
    position: absolute; bottom: 34px; width: 100%;
    text-align: center; font-size: 13px; color: var(--ink-grey);
  }
</style>
</head>
<body>
<main class="canvas">
  <section class="card card--front">
    <div class="brand">
      <span class="brand-dot"></span>
      <span class="brand-name">KESTRAVOLT</span>
    </div>
    <div class="rule rule--upper"></div>
    <div class="holder">
      <p class="holder-name">Marcus Lin Ho, PhD</p>
      <p class="holder-cn">何林 博士</p>
      <p class="holder-role">CEO</p>
    </div>
    <div class="office office--cn">
      <p class="office-label">China</p>
      <p>1806, NO.88 Xinhua Road, Dongcheng</p>
      <p>District, Beijing, China 100010</p>
      <p>北京市东城区新华路88号明辉大厦</p>
      <p>http://www.luminhall.com</p>
    </div>
    <div class="rule rule--lower"></div>
    <div class="office office--us">
      <p class="office-label">U.S.</p>
      <p>4820 Harbor Crest Way, Suite 210</p>
      <p>Alder Bay, CA 94512</p>
      <p>Email: mho@kestravolt.com</p>
      <p>Cell: 707-555-0147</p>
      <p>http://www.kestravolt.com</p>
    </div>
  </section>

  <section class="card card--back">
    <div class="brand">
      <span class="brand-dot"></span>
      <span class="brand-name">KESTRAVOLT</span>
    </div>
    <p class="back-url">www.kestravolt.com</p>
  </section>
</main>
</body>
</html>
```